Brightvale Fluid Systems Corp Business Cards

Business cards to match the logo.

Company is a start up water technology company that has developed a patented system using centrifugal force to separate waste from municipal waste water to produce crystal clear clean water. Product sell starting at 2 million to governments both in the US and international.

Business cards should have a professional look with the target generally engineers.

Target Market(s)

Engineers, Government officials and investors

Industry/Entity Type

Water Treatment

Contact Information for Business Card

Business cards design will be used for 6 to 8 people with job titles. Can use the quote "If there is magic in the planet, it is contained in water." but not required to use quote. Should follow theme of Logo

Font styles to use
Other font styles liked:
• match logo font

Requirements
Nice to have
• Colors to match Logo. Business cards to match style of flow of Logo.
• Emphasis on clean look not a busy look. Clean flowing water.
Should not have
• Pictures of industrial equipment or wastewater

```html
<!DOCTYPE html>
<html lang="en">
<head>
<meta charset="utf-8">
<title>Brightvale Fluid Systems Corp — Business Cards</title>
<link rel="stylesheet" href="https://fonts.googleapis.com/css2?family=Playfair+Display:wght@400&family=Open+Sans:wght@400&display=swap">
<style>
  :root {
    --bg: #5a5a5a;
    --sky: #29a8e0;
    --deep: #12548a;
    --paper: #ffffff;
    --quote: #6f6f6f;
    --serif: "Playfair Display", Georgia, serif;
    --sans: "Open Sans", Arial, sans-serif;
  }
  * { margin: 0; padding: 0; box-sizing: border-box; }
  html, body { width: 1200px; height: 1200px; overflow: hidden; background: var(--bg); }
  .sheet { position: relative; width: 1200px; height: 1200px; }
  .card {
    position: absolute; left: 150px; width: 900px; height: 514px;
    overflow: hidden; box-shadow: 0 10px 30px rgba(0,0,0,.35);
  }
  .card--front { top: 56px; background: var(--sky); display: flex; align-items: center; justify-content: center; }
  .card--back { top: 630px; background: var(--paper); }
  .wordmark { font-family: var(--serif); font-weight: 400; line-height: 1.1; white-space: nowrap; }
  .card--front .wordmark { color: var(--paper); font-size: 58px; letter-spacing: 2px; }
  .card--back .wordmark { position: absolute; left: 56px; top: 104px; color: var(--deep); font-size: 34px; }
  .wave { position: absolute; inset: 0; width: 900px; height: 514px; }
  .quote {
    position: absolute; left: 470px; top: 30px; width: 400px;
    font-family: var(--serif); color: var(--quote); font-size: 19px; line-height: 1.4;
  }
  .quote-mark { font-size: 30px; color: #9a9a9a; vertical-align: -8px; line-height: 0; }
  .contact { position: absolute; left: 560px; top: 190px; list-style: none; }
  .contact li {
    display: flex; align-items: center; gap: 14px; height: 34px;
    font-family: var(--sans); color: var(--paper); font-size: 21px; white-space: nowrap;
  }
  .contact svg { width: 20px; height: 20px; flex: none; }
  .person { position: absolute; left: 80px; top: 296px; }
  .person-name { font-family: var(--serif); color: var(--deep); font-size: 50px; line-height: 1.1; white-space: nowrap; }
  .person-title { font-family: var(--sans); color: var(--paper); font-size: 24px; margin: 4px 0 0 150px; white-space: nowrap; }
  .divider { position: absolute; left: 560px; top: 352px; width: 160px; height: 1.5px; background: var(--paper); }
  .address { position: absolute; left: 240px; top: 440px; font-family: var(--sans); color: var(--paper); font-size: 21px; white-space: nowrap; }
</style>
</head>
<body>
<main class="sheet">
  <section class="card card--front" aria-label="Card front">
    <p class="wordmark">Brightvale Fluid Systems</p>
  </section>

  <section class="card card--back" aria-label="Card back">
    <svg class="wave" viewBox="0 0 900 514" aria-hidden="true">
      <path fill="var(--deep)" d="M0,232 C250,230 380,205 500,160 C620,118 740,110 900,104 L900,514 L0,514 Z"/>
      <path fill="var(--sky)" d="M0,252 C260,250 400,226 520,182 C640,140 760,132 900,128 L900,514 L0,514 Z"/>
    </svg>

    <p class="wordmark">Brightvale Fluid Systems</p>

    <p class="quote"><span class="quote-mark">“</span> If there is magic in the planet,<br>it is contained in water. <span class="quote-mark">”</span></p>

    <ul class="contact">
      <li><svg viewBox="0 0 20 20"><rect x="5" y="1.5" width="10" height="17" rx="2" fill="none" stroke="#fff" stroke-width="1.6"/><circle cx="10" cy="15.5" r="1" fill="#fff"/></svg>(555) 014-2287</li>
      <li><svg viewBox="0 0 20 20"><path fill="#fff" d="M5 2 L8 2 L9 6 L7 8 C8 11 9 12 12 13 L14 11 L18 12 L18 15 C18 17 16 18 14 18 C7 17 3 13 2 6 C2 4 3 2 5 2 Z"/></svg>(555) 019-6630</li>
      <li><svg viewBox="0 0 20 20"><rect x="1.5" y="4" width="17" height="12" fill="#fff"/><path d="M1.5 4 L10 11 L18.5 4" fill="none" stroke="var(--sky)" stroke-width="1.5"/></svg>cwhitlock@brightvalefs.com</li>
      <li><svg viewBox="0 0 20 20" fill="none" stroke="#fff" stroke-width="1.3"><circle cx="10" cy="10" r="8"/><ellipse cx="10" cy="10" rx="3.5" ry="8"/><path d="M2 10 H18 M3.5 6 H16.5 M3.5 14 H16.5"/></svg>www.brightvalefs.com</li>
    </ul>

    <div class="divider"></div>

    <div class="person">
      <p class="person-name">Corin Whitlock</p>
      <p class="person-title">Senior Engineer</p>
    </div>

    <p class="address">2480 Harbor Crest Rd, Suite 210, Lakemont 40211</p>
  </section>
</main>
</body>
</html>
```